Letterhead for New Orthopaedic Surgery Practice

My husband and I are starting our own practice named RB Spine & Vitality Center. We would like to create a nice simple but high class letterhead that doesn't use too much solid color ink when printing. I like the colors dark blue, gold, yellow. Open to other suggestions. We will need to list him and I both on the top of the letterhead. Here is the important information:
Lucinda Perrow, M.D. - Hand and Upper Extremity Surgery
Abena Quist, M.D. - Hip & Knee Replacement/General Orthopaedic Surgery
Location: 18735 North Harlow Pkwy
Palm Ridge, FL 33488
Phone: 954-218-4650
Fax: 954-582-1346
Email: info@myrbspine.com

The only thing is that the phone and fax numbers will change once we get into our space. I just want to get the design started. I am including several documents which are my previous practice letterhead, my current procedure room letterhead, and our new Logo. The other letterheads are just for examples but please think outside of the box! We would love to see some great designs.

Colors
0054AA
0677BA
7BADD7
CADEEF
E8F1F8
0094D4
00A9DD
6FCCEA
C7EBF8
E9F6FB

Requirements
Must have
• class, elegance, luxury

```html
<!DOCTYPE html>
<html lang="en">
<head>
<meta charset="utf-8">
<title>RB Spine &amp; Vitality Center — Letterhead</title>
<link rel="stylesheet" href="https://fonts.googleapis.com/css2?family=Montserrat:wght@400;600;700&display=swap">
<style>
  :root {
    --navy: #1f3f8f;
    --cyan: #00a9dd;
    --sky: #0094d4;
    --slate: #7b8db5;
    --ink: #2b2b2b;
    --muted: #6a6a6a;
    --leaf-a: #e8f1f8;
    --leaf-b: #f4f8fc;
    --backdrop: #efefef;
    --paper: #ffffff;
  }
  * { margin: 0; padding: 0; box-sizing: border-box; }
  html, body {
    width: 1102px; height: 1200px; overflow: hidden;
    background: var(--backdrop);
    font-family: "Montserrat", sans-serif;
  }
  .letterhead {
    position: absolute; left: 141px; top: 20px;
    width: 820px; height: 1160px;
    background: var(--paper);
    overflow: hidden;
  }
  .brand {
    position: absolute; left: 70px; top: 70px;
    display: flex; align-items: center; gap: 16px;
  }
  .brand-mark { width: 70px; height: 70px; background: var(--navy); flex: none; }
  .brand-name {
    font-size: 22px; font-weight: 600; color: var(--navy);
    letter-spacing: 0.5px; text-transform: uppercase; line-height: 26px;
  }
  .contact {
    position: absolute; right: 70px; top: 99px;
    text-align: right; color: var(--cyan);
    font-size: 10.5px; font-weight: 700; line-height: 14px;
    letter-spacing: 0.4px; font-style: normal;
  }
  .contact .gap { height: 12px; }
  .header-rule {
    position: absolute; left: 70px; top: 227px; width: 681px; height: 2px;
    background: linear-gradient(to right, var(--cyan) 0 46%, var(--slate) 46% 100%);
  }
  .physicians { position: absolute; left: 101px; top: 311px; }
  .physician { margin-bottom: 13px; }
  .physician-name {
    color: var(--sky); font-size: 12.5px; font-weight: 700; letter-spacing: 0.4px;
  }
  .physician-role { color: var(--muted); font-size: 8.5px; margin-top: 3px; }
  .letter-body {
    position: absolute; left: 101px; top: 420px; width: 615px;
    color: var(--ink); font-size: 9.2px; line-height: 20.8px;
    text-align: justify; letter-spacing: 0.45px;
  }
  .foliage {
    position: absolute; left: 0; bottom: 0; width: 820px; height: 280px;
    background: radial-gradient(ellipse at 50% 80%, var(--leaf-a) 0%, var(--leaf-b) 60%, var(--paper) 100%);
  }
  .signature {
    position: absolute; width: 170px; height: 68px;
    background: linear-gradient(to right, #f2f2f2, #e9e9e9);
    border-radius: 4px;
  }
  .sig-perrow { left: 106px; top: 845px; }
  .sig-quist { left: 496px; top: 840px; }
  .signatory { position: absolute; top: 929px; }
  .signatory-perrow { left: 130px; }
  .signatory-quist { left: 511px; }
  .signatory-name { color: var(--ink); font-size: 10px; font-weight: 700; letter-spacing: 0.4px; }
  .signatory-role { color: var(--muted); font-size: 7px; margin-top: 4px; }
</style>
</head>
<body>
<main class="letterhead">
  <div class="foliage" role="img" aria-label="Faint pale blue leafy branch decoration across the lower page"></div>

  <div class="brand">
    <span class="brand-mark"></span>
    <span class="brand-name">RB Spine &amp;<br>Vitality Center</span>
  </div>

  <address class="contact">
    <div>18735 North Harlow Pkwy</div>
    <div>Palm Ridge, FL 33488</div>
    <div class="gap"></div>
    <div>FAX: 954-582-1346</div>
    <div>Phone: 954-218-4650</div>
    <div class="gap"></div>
    <div>info@myrbspine.com</div>
  </address>

  <div class="header-rule"></div>

  <section class="physicians">
    <div class="physician">
      <div class="physician-name">Lucinda Perrow, M.D.</div>
      <div class="physician-role">Hand and Upper Extremity Surgery</div>
    </div>
    <div class="physician">
      <div class="physician-name">Abena Quist, M.D.</div>
      <div class="physician-role">Hip &amp; Knee Replacement/General Orthopaedic Surgery</div>
    </div>
  </section>

  <section class="letter-body">
    <p>Lorem ipsum dolor sit amet, consectetuer adipiscing elit, sed diam nonummy nibh euismod tincidunt ut laoreet dolore magna aliquam erat volutpat. Ut wisi enim ad minim veniam, quis nostrud exerci tation ullamcorper suscipit lobortis nisl ut aliquip ex ea commodo consequat. Duis autem vel eum iriure dolor in hendrerit in vulputate velit esse molestie consequat, vel illum dolore eu feugiat nulla facilisis at vero eros et accumsan et iusto odio dignissim qui blandit praesent luptatum zzril delenit augue duis dolore te feugait nulla facilisi.</p>
    <p>Lorem ipsum dolor sit amet, cons ectetuer adipiscing elit, sed diam nonummy nibh euismod tincidunt ut laoreet dolore magna aliquam erat volutpat. Ut wisi enim ad minim veniam, quis nostrud exerci tation ullamcorper suscipit lobortis nisl ut aliquip ex ea commodo consequat.</p>
    <p>Lorem ipsum dolor sit amet, consectetuer adipiscing elit, sed diam nonummy nibh euismod tincidunt ut laoreet dolore magna aliquam erat volutpat. Ut wisi enim ad minim veniam, quis nostrud exerci tation ullamcorper suscipit lobortis nisl ut aliquip ex ea commodo consequat. Duis autem vel eum iriure dolor in hendrerit in vulputate velit esse molestie consequat, vel illum dolore eu feugiat nulla facilisis at vero eros et accumsan et iusto odio dignissim qui blandit praesent luptatum zzril delenit augue duis dolore te feugait nulla facilisi.</p>
    <p>Lorem ipsum dolor sit amet, cons ectetuer adipiscing elit, sed diam nonummy nibh euismod tincidunt ut laoreet dolore magna aliquam erat volutpat. Ut wisi enim ad minim veniam, quis nostrud exerci tation ullamcorper suscipit lobortis nisl ut aliquip ex ea commodo consequat.</p>
  </section>

  <div class="signature sig-perrow" role="img" aria-label="Handwritten signature of Lucinda Perrow"></div>
  <div class="signature sig-quist" role="img" aria-label="Handwritten signature of Abena Quist"></div>

  <div class="signatory signatory-perrow">
    <div class="signatory-name">Lucinda Perrow, M.D.</div>
    <div class="signatory-role">Hand and Upper Extremity Surgery</div>
  </div>
  <div class="signatory signatory-quist">
    <div class="signatory-name">Abena Quist, M.D.</div>
    <div class="signatory-role">Hip &amp; Knee Replacement/General Orthopaedic Surgery</div>
  </div>
</main>
</body>
</html>
```